Hair Extension Package

I need a high end looking package design for hair extensions. It must include our company logo (either black or white version) and the text that is provided in the attachment. The image of the old package is for dimension purposes only.
Updates
I have added an image of the dimensions the package needs to be.
Thanks
Target Market(s)
Salons and hairdressers would be purchasing this product
Industry/Entity Type
Hair
Look and feel
Each slider illustrates characteristics of the customer's brand and the style your logo design should communicate.

```html
<!DOCTYPE html>
<html lang="en">
<head>
<meta charset="utf-8">
<title>Lumen Locks – Hair Extension Package</title>
<link href="https://fonts.googleapis.com/css2?family=Roboto:ital,wght@0,400;0,700;1,400&family=Roboto+Condensed:ital,wght@0,400;0,700;1,400&display=swap" rel="stylesheet">
<style>
  :root {
    --ink: #000000;
    --panel-grey: #e4e4e4;
    --panel-grey-dark: #cfcfcf;
    --frame: #6b6b6b;
    --cyan: #1eaee8;
    --pink: #d6246e;
    --white: #ffffff;
    --hair-dark: #4a3a30;
    --hair-light: #8c7868;
    --band-dark: #2a2a2a;
  }
  * { box-sizing: border-box; margin: 0; padding: 0; }
  html, body { width: 750px; height: 1200px; overflow: hidden; background: var(--white); }
  .canvas { position: relative; width: 750px; height: 1200px; font-family: "Roboto", Arial, sans-serif; }

  /* Header card (front flap) */
  .header-card {
    position: absolute; width: 133px; height: 210px;
    background: linear-gradient(180deg, #ffffff 0%, #eeeeee 60%, #bdbdbd 100%);
    border: 2px solid var(--frame);
    border-bottom-left-radius: 6px 14px;
    border-bottom-right-radius: 6px 14px;
    overflow: hidden;
  }
  .header-card .brand-band {
    position: absolute; left: 0; top: 0; width: 100%; height: 40px;
    background: var(--ink); display: flex; align-items: center; justify-content: center;
  }
  .brand-name {
    font-family: "Roboto Condensed", Arial, sans-serif; font-weight: 700;
    color: var(--white); font-size: 17px; letter-spacing: 0.5px;
  }
  .header-card .product-photo {
    position: absolute; left: 24px; top: 46px; width: 88px; height: 112px;
    border-radius: 40px 40px 6px 6px;
    background: linear-gradient(180deg, var(--hair-light) 0%, var(--hair-dark) 70%, #2e241d 100%);
  }
  .header-card .curve { position: absolute; left: 0; top: 138px; width: 100%; height: 72px; }
  .header-card .claim {
    position: absolute; left: 10px; top: 164px; width: 130px;
    transform: rotate(-13deg); transform-origin: left top;
    font-weight: 700; font-size: 7.2px; color: var(--cyan); white-space: nowrap;
  }
  .header-card .site {
    position: absolute; left: 38px; top: 181px;
    transform: rotate(-13deg); transform-origin: left top;
    font-weight: 700; font-size: 5.4px; color: var(--ink); white-space: nowrap;
  }

  /* Back strip */
  .back-strip {
    position: absolute; left: 55px; top: 221px; width: 133px; height: 960px;
    background: var(--ink); color: var(--white);
  }
  .hang-hole { position: absolute; top: 63px; width: 5px; height: 5px; border-radius: 50%; background: var(--white); }
  .tagline {
    position: absolute; left: 4px; top: 103px; width: 125px;
    font-family: "Roboto Condensed", Arial, sans-serif; font-style: italic;
    font-size: 6.4px; line-height: 8.3px; text-align: center;
  }
  .divider { position: absolute; left: 0; top: 145px; width: 100%; border-top: 1px dashed #555; }
  .care-title {
    position: absolute; left: 0; top: 159px; width: 100%; text-align: center;
    font-family: "Roboto Condensed", Arial, sans-serif; color: var(--cyan); font-size: 11px;
  }
  .care-list {
    position: absolute; left: 8px; top: 182px; width: 122px; list-style: none;
    font-size: 6.9px; line-height: 8.65px;
  }
  .care-list li { position: relative; padding-left: 6px; }
  .care-list li::before { content: "•"; position: absolute; left: 0; color: var(--pink); }
  .spec-label {
    position: absolute; left: 7px; top: 804px; width: 119px; height: 78px;
    background: var(--white); border-radius: 7px; color: var(--ink);
  }
  .spec-label .name-bar { position: absolute; left: 8px; top: 6px; width: 102px; height: 18px; background: var(--ink); border-radius: 6px; }
  .spec-label .field { position: absolute; left: 11px; font-size: 5.6px; font-weight: 700; }
  .spec-label .field span { display: inline-block; width: 68px; border-bottom: 0.6px solid var(--ink); margin-left: 2px; }
  .bin-icon { position: absolute; left: 93px; top: 917px; }

  /* Front strips */
  .front-strip {
    position: absolute; top: 218px; width: 135px; height: 959px;
    background: linear-gradient(160deg, var(--panel-grey) 0%, #f1f1f1 45%, var(--panel-grey-dark) 100%);
    border: 2px solid var(--frame);
  }
  .front-strip .figure-art {
    position: absolute; left: 30px; top: 702px; width: 75px; height: 165px;
    background: radial-gradient(ellipse at 50% 45%, #c9c9c9 0%, rgba(210,210,210,0) 70%);
  }
  .front-strip .footer-band {
    position: absolute; left: 0; bottom: 14px; width: 100%; height: 46px;
    background: linear-gradient(180deg, #111 0%, var(--band-dark) 70%, #8a8a8a 100%);
    display: flex; align-items: center; justify-content: center;
  }
  .left-header { left: 55px; top: 12px; transform: rotate(180deg); }
  .flap-header { left: 255px; top: 220px; transform: skewX(25deg); transform-origin: left top; height: 196px; }
  .right-header { left: 535px; top: 220px; }
</style>
</head>
<body>
<div class="canvas">

  <!-- Back panel -->
  <div class="header-card left-header">
    <div class="brand-band"><span class="brand-name">LUMEN LOCKS</span></div>
    <div class="product-photo" role="img" aria-label="Photo of a model with long straight brown hair"></div>
    <svg class="curve" viewBox="0 0 133 72" preserveAspectRatio="none">
      <path d="M0 28 Q60 0 133 8 L133 72 L0 72 Z" fill="#ffffff"/>
      <path d="M0 56 Q60 34 133 40" stroke="#222" stroke-width="2" fill="none"/>
      <path d="M0 62 Q60 40 133 46" stroke="#888" stroke-width="1.5" fill="none"/>
    </svg>
    <div class="claim">PREMIUM REMY HUMAN HAIR</div>
    <div class="site">WWW.LUMENLOCKS.COM</div>
  </div>

  <div class="back-strip">
    <span class="hang-hole" style="left:42px"></span>
    <span class="hang-hole" style="left:87px"></span>
    <p class="tagline">Exquisite craftmanship for soft &amp; micro thin hair,<br>Tangle &amp; Shed resistant<br>Reusable &amp; Long lasting</p>
    <div class="divider"></div>
    <h2 class="care-title">Hair Care Instructions</h2>
    <ul class="care-list">
      <li>Brush your extensions from the ends up. When brushing your extensions always start with the ends and move up towards the scalp. This reduces the possibility of shedding and makes it easier to remove tangles.</li>
      <li>Use of cotton pillowcases and sheets may adversely affect the shine of your hair, use a silk or satin sleep cap to wrap up your hair.</li>
      <li>Use quality products on your extensions. Always use a light moisturizer or leave-in conditioner to keep the hair extensions moisturized since it doesn't benefit from the natural oils produced by your scalp. Do not use harsh product such as those containing alcohol on your extensions.</li>
      <li>Before shampooing, gently remove any tangles. If hair is excessively tangled, a spray on conditioner should be used.</li>
      <li>Always use a mild shampoo or a sulphate free shampoo.</li>
      <li>Run the hair under warm water and after placing a small amount of shampoo on your fingers, gently work the shampoo into the hair, stroking downwards from the weft base to the ends. Do not twist, scrub or rub the hair. Use the shampoo sparingly.</li>
      <li>When clean, rinse thoroughly under warm running water until the water runs clear. Be sure to rinse until all shampoo is removed, as improper rinsing could result in damage.</li>
      <li>Just like your own hair, human hair extensions need to be conditioned after shampooing to maintain a healthy shine and promote styling ease.</li>
      <li>Place a small amount of conditioner in your hand. Gently work into the hair and let sit for three to five minutes.</li>
      <li>Rinse thoroughly in warm water.</li>
      <li>Gently towel blot to remove excess water.</li>
      <li>While wet, gently comb the hair to remove tangles. Using a large toothed comb, move in a downward motion away from the tracks and to the ends. Do not use a bristle brush on wet hair as it may pull out or break the hair.</li>
    </ul>
    <div class="spec-label">
      <div class="name-bar"></div>
      <div class="field" style="top:35px">COLOUR:<span></span></div>
      <div class="field" style="top:48px">LENGTH:<span></span></div>
      <div class="field" style="top:61px">TEXTURE:<span></span></div>
    </div>
    <svg class="bin-icon" width="20" height="28" viewBox="0 0 20 28" fill="none" stroke="#ffffff" stroke-width="1">
      <circle cx="9" cy="3" r="2"/>
      <path d="M9 5 L8 14 L5 26 M8 14 L12 26 M4 9 L14 9"/>
      <path d="M13 16 L19 16 L18 27 L14 27 Z"/>
    </svg>
  </div>

  <!-- Front panel with open flap -->
  <div class="front-strip" style="left:253px">
    <div class="figure-art" role="img" aria-label="Line illustration of a woman's profile with flowing hair"></div>
    <div class="footer-band"><span class="brand-name">LUMEN LOCKS</span></div>
  </div>
  <div class="header-card flap-header">
    <div class="brand-band"><span class="brand-name">LUMEN LOCKS</span></div>
    <div class="product-photo" role="img" aria-label="Photo of a model with long straight brown hair"></div>
    <svg class="curve" viewBox="0 0 133 72" preserveAspectRatio="none">
      <path d="M0 28 Q60 0 133 8 L133 72 L0 72 Z" fill="#ffffff"/>
      <path d="M0 56 Q60 34 133 40" stroke="#222" stroke-width="2" fill="none"/>
      <path d="M0 62 Q60 40 133 46" stroke="#888" stroke-width="1.5" fill="none"/>
    </svg>
    <div class="claim">PREMIUM REMY HUMAN HAIR</div>
    <div class="site">WWW.LUMENLOCKS.COM</div>
  </div>

  <!-- Front panel closed -->
  <div class="front-strip" style="left:535px">
    <div class="figure-art" role="img" aria-label="Line illustration of a woman's profile with flowing hair"></div>
    <div class="footer-band"><span class="brand-name">LUMEN LOCKS</span></div>
  </div>
  <div class="header-card right-header">
    <div class="brand-band"><span class="brand-name">LUMEN LOCKS</span></div>
    <div class="product-photo" role="img" aria-label="Photo of a model with long straight brown hair"></div>
    <svg class="curve" viewBox="0 0 133 72" preserveAspectRatio="none">
      <path d="M0 28 Q60 0 133 8 L133 72 L0 72 Z" fill="#ffffff"/>
      <path d="M0 56 Q60 34 133 40" stroke="#222" stroke-width="2" fill="none"/>
      <path d="M0 62 Q60 40 133 46" stroke="#888" stroke-width="1.5" fill="none"/>
    </svg>
    <div class="claim">PREMIUM REMY HUMAN HAIR</div>
    <div class="site">WWW.LUMENLOCKS.COM</div>
  </div>

</div>
</body>
</html>
```